Business Card and Stationary for KVT Builders
Need standard business card, letterhead, and envelopes to incorporate our new logo
Business Card and Stationary for KVT Builders - Construction
Creative Brief
Simple
Rowan Pelley
Vice President
4621 Brantwell Houston, TX 77031
rowan@kvtbuilders.example
I'm open to layout ideas for all designs. letterhead and envelopes need to be accessible to incorporate microsoft office products.

```html
<!DOCTYPE html>
<html lang="en">
<head>
<meta charset="utf-8">
<title>KVT Builders Stationery</title>
<link href="https://fonts.googleapis.com/css2?family=Open+Sans:ital,wght@0,400;0,700;0,800;1,400&display=swap" rel="stylesheet">
<style>
:root{
  --blue:#4a4bb0;
  --blue-dark:#3a3b96;
  --gray:#8a8b90;
  --gray-light:#c9cacd;
  --paper:#ffffff;
  --ink:#5a5b62;
  --bg:#e6e6e8;
}
*{margin:0;padding:0;box-sizing:border-box}
html,body{width:1200px;height:833px;overflow:hidden}
body{background:var(--bg);font-family:"Open Sans",Arial,sans-serif;color:var(--ink);position:relative}
.piece{position:absolute;background:var(--paper);box-shadow:0 2px 6px rgba(0,0,0,.18);overflow:hidden}
.brand{font-weight:800;color:var(--blue);white-space:nowrap;line-height:1}
.brand.light{color:#fff}
.tagline{font-style:italic;font-size:9px;color:var(--blue);letter-spacing:.2px}

/* envelopes (backs) */
.envelope-back{left:40px;width:400px;height:180px}
.envelope-back svg{position:absolute;inset:0}
.envelope-back .brand{position:absolute;left:0;right:0;top:34px;text-align:center;font-size:22px}
.env-1{top:30px}
.env-2{top:160px}
.env-3{top:290px}

/* envelope front */
.envelope-front{left:40px;top:480px;width:400px;height:200px}
.envelope-front .brand{position:absolute;left:24px;top:26px;font-size:24px}
.envelope-front .tagline{position:absolute;left:24px;top:54px}
.envelope-front .return{position:absolute;left:24px;top:70px;font-size:8px}
.envelope-front .band{position:absolute;left:0;right:0;bottom:0;height:14px;background:var(--blue)}

/* letterhead */
.letterhead{left:470px;top:30px;width:440px;height:780px;padding:40px 46px 0}
.letterhead .head{text-align:center;margin-bottom:22px}
.letterhead .head .brand{font-size:26px}
.letterhead .head .tagline{margin-top:4px}
.letterhead .recipient,.letterhead p{font-size:10px;line-height:1.45}
.letterhead .recipient{margin-bottom:14px}
.letterhead p{margin-bottom:12px;color:#7a7b82}
.letterhead .closing{margin-top:18px;font-size:10px;line-height:1.45}
.letterhead .signature-space{height:34px}
.letterhead .footer{position:absolute;left:0;right:0;bottom:0;height:30px;border-top:3px solid var(--blue);font-size:7px;text-align:center;padding-top:8px;color:var(--ink)}

/* business cards */
.card{left:960px;width:200px;height:112px}
.card .brand{font-size:20px}
.card .center{position:absolute;left:0;right:0;top:34px;text-align:center}
.card .url{font-size:8px;margin-top:12px;color:var(--ink)}
.card.blue{background:var(--blue)}
.card.gray{background:var(--gray)}
.card.blue .url,.card.gray .url{color:#fff}
.card-1{top:40px}
.card-2{top:195px}
.card-3{top:350px}
.card-4{top:505px}
.card-5{top:660px}
.card .stripe{position:absolute;left:0;right:0;bottom:0;height:8px;background:var(--blue)}
.card .detail-brand{position:absolute;left:12px;top:26px;font-size:16px}
.card .detail-brand + .tagline{position:absolute;left:12px;top:46px;font-size:7px}
.card .person{position:absolute;right:12px;top:26px;text-align:right;font-size:9px;font-weight:700;color:var(--blue)}
.card .person span{display:block;font-weight:400;font-size:7px;color:var(--ink)}
.card .contact{position:absolute;left:12px;top:62px;font-size:6.5px;line-height:1.45}
</style>
</head>
<body>

<section class="piece envelope-back env-1" aria-label="Envelope back, white flap">
  <svg width="400" height="180"><polygon points="0,0 400,0 200,120" fill="#f2f2f4" stroke="#d8d8dc"/></svg>
  <div class="brand">KVT Builders</div>
</section>

<section class="piece envelope-back env-2" aria-label="Envelope back, blue flap">
  <svg width="400" height="180"><polygon points="0,0 400,0 200,120" fill="var(--blue)"/></svg>
  <div class="brand light">KVT Builders</div>
</section>

<section class="piece envelope-back env-3" aria-label="Envelope back, gray flap">
  <svg width="400" height="180"><polygon points="0,0 400,0 200,120" fill="var(--gray)"/></svg>
  <div class="brand light">KVT Builders</div>
</section>

<section class="piece envelope-front" aria-label="Envelope front">
  <div class="brand">KVT Builders</div>
  <div class="tagline">Commercial Concrete Contractors</div>
  <div class="return">4621 Brantwell Houston, TX 77031</div>
  <div class="band"></div>
</section>

<section class="piece letterhead">
  <header class="head">
    <div class="brand">KVT Builders</div>
    <div class="tagline">Commercial Concrete Contractors</div>
  </header>
  <div class="recipient">Someone Some body<br>12 Harlow Lane<br>Westbury<br><br>Dear Someone Somebody,</div>
  <p>Lorem ipsum dolor sit amet, consectetuer adipiscing elit, sed diam nonummy nibh euismod tincidunt ut laoreet dolore magna aliquam erat volutpat. Ut wisi enim ad minim veniam, quis nostrud exerci tation ullamcorper suscipit lobortis nisl ut aliquip ex ea commodo consequat. Duis autem vel eum iriure dolor in hendrerit in vulputate velit esse molestie consequat, vel illum dolore eu feugiat nulla facilisis at vero eros et accumsan et iusto odio dignissim qui blandit praesent luptatum zzril delenit augue duis dolore te feugait nulla facilisi.</p>
  <p>Lorem ipsum dolor sit amet, consectetuer adipiscing elit, sed diam nonummy nibh euismod tincidunt ut laoreet dolore magna aliquam erat volutpat. Ut wisi enim ad minim veniam, quis nostrud exerci tation ullamcorper suscipit lobortis nisl ut aliquip ex ea commodo consequat. Duis autem vel eum iriure dolor in hendrerit in vulputate velit esse molestie consequat, vel illum dolore eu feugiat nulla facilisis at vero eros et accumsan et iusto odio dignissim qui blandit praesent luptatum zzril delenit augue duis dolore te feugait nulla facilisi.</p>
  <p>Lorem ipsum dolor sit amet, consectetuer adipiscing elit, sed diam nonummy nibh euismod tincidunt ut laoreet dolore magna aliquam erat volutpat. Ut wisi enim ad minim veniam, quis nostrud exerci tation ullamcorper suscipit lobortis nisl ut aliquip ex ea commodo consequat. Duis autem vel eum iriure dolor in hendrerit in vulputate velit esse molestie consequat, vel illum dolore eu feugiat nulla facilisis at vero eros et accumsan et iusto odio dignissim qui blandit praesent luptatum zzril delenit augue duis dolore te feugait nulla facilisi.</p>
  <div class="closing">Yours Sincerely,<br>Marcus Ellery<div class="signature-space"></div></div>
  <footer class="footer">4621 Brantwell Houston, TX 77031 &nbsp;|&nbsp; P (713) 555-0142 &nbsp;|&nbsp; F (713) 555-0143 &nbsp;|&nbsp; rowan@kvtbuilders.example</footer>
</section>

<section class="piece card card-1">
  <div class="center"><div class="brand">KVT Builders</div><div class="url">www.kvtbuilders.example</div></div>
</section>

<section class="piece card card-2 blue">
  <div class="center" style="top:44px"><div class="brand light">KVT Builders</div></div>
</section>

<section class="piece card card-3 gray">
  <div class="center"><div class="brand light">KVT Builders</div><div class="url">www.kvtbuilders.example</div></div>
</section>

<section class="piece card card-4">
  <div class="brand detail-brand">KVT Builders</div>
  <div class="tagline">Commercial Concrete Contractors</div>
  <div class="person">Rowan Pelley<span>Vice President</span></div>
  <div class="contact">P (713) 555-0142<br>M (713) 555-0177<br>rowan@kvtbuilders.example</div>
  <div class="stripe"></div>
</section>

<section class="piece card card-5">
  <div class="person" style="left:12px;right:auto;text-align:left;top:14px">Rowan Pelley<span>Vice President</span></div>
  <div class="contact" style="top:40px">P (713) 555-0142<br>M (713) 555-0177<br>rowan@kvtbuilders.example</div>
  <div class="brand detail-brand" style="left:auto;right:12px;top:70px">KVT Builders</div>
  <div class="stripe"></div>
</section>

</body>
</html>
```